Help keep hoosiers happy and at home!

We need a billboard designed for our Indiana based healthcare business called 'Harbor Lane Home Aides'. We administer a medicaid waiver program that provides support and financial aid to live in caregivers that take care of someone who would otherwise be in a nursing home or skilled nursing facility. Qualified caregivers could be eligible to receive up to 1200 dollars a month in tax free financial aid, as well as access to nursing support that helps manage any unexpected situations or changes in a care recipients condition or care routine. Our program empowers families to keep their loved ones at home and out of the nursing home. NOTE: We believe the tagline at the bottom of our logo is disproportionately small. We would like to see that tagline larger and easier to read. I look forward to seeing your design ideas!

Target Market(s)

Medicaid aged beneficiaries and caregivers.

Industry/Entity Type

Home Healthcare

Colors
0054AA
0677BA
7BADD7
CADEEF
E8F1F8

Requirements
Nice to have
• "Empowering friends and family to care for their loves ones at home. Eligible participants receive up to $15,000 a year, tax free."

```html
<!DOCTYPE html>
<html lang="en">
<head>
<meta charset="utf-8">
<title>Harbor Lane Home Aides – Billboard</title>
<link rel="stylesheet" href="https://fonts.googleapis.com/css2?family=Bebas+Neue&family=Montserrat:wght@700&family=Poppins:wght@400;700&display=swap">
<style>
  :root {
    --navy: #2e3580;
    --blue: #0054aa;
    --stripe: #0a56ab;
    --panel: #0f5aad;
    --deep: #071f7a;
    --accent: #0677ba;
    --white: #ffffff;
    --backdrop: #e6e7e9;
    --photo-dark: #4c5a4a;
    --photo-mid: #9a8a6e;
    --photo-light: #e6d6bd;
  }
  * { margin: 0; padding: 0; box-sizing: border-box; }
  html, body {
    width: 1200px;
    height: 1000px;
    overflow: hidden;
    background: var(--backdrop);
  }
  .billboard {
    position: absolute;
    left: 108px;
    top: 290px;
    width: 985px;
    height: 429px;
    background: var(--white);
    overflow: hidden;
  }
  .billboard-shapes {
    position: absolute;
    inset: 0;
    width: 985px;
    height: 429px;
  }
  .brand {
    position: absolute;
    left: 35px;
    top: 62px;
    display: flex;
    align-items: center;
    gap: 10px;
  }
  .brand-dot {
    width: 26px;
    height: 26px;
    border-radius: 50%;
    background: var(--navy);
  }
  .brand-name {
    font-family: "Poppins", sans-serif;
    font-weight: 400;
    font-size: 17px;
    color: var(--navy);
    letter-spacing: 0.02em;
  }
  .headline {
    position: absolute;
    left: 34px;
    top: 170px;
    font-family: "Bebas Neue", sans-serif;
    font-weight: 400;
    font-size: 60px;
    line-height: 71px;
    color: var(--navy);
    white-space: nowrap;
  }
  .headline .highlight { color: var(--blue); }
  .message {
    position: absolute;
    left: 34px;
    top: 334px;
    font-family: "Montserrat", sans-serif;
    font-weight: 700;
    font-size: 12px;
    line-height: 23.5px;
    color: var(--navy);
    white-space: nowrap;
  }
  .message .highlight { color: var(--accent); }
  .contact {
    position: absolute;
    left: 640px;
    top: 322px;
    width: 305px;
    text-align: center;
    font-family: "Poppins", sans-serif;
    font-weight: 700;
    color: var(--white);
  }
  .contact-label {
    font-size: 22px;
    line-height: 1.2;
    letter-spacing: 0.03em;
  }
  .contact-phone {
    margin-top: 9px;
    font-size: 29px;
    line-height: 1.2;
    letter-spacing: 0.03em;
  }
</style>
</head>
<body>
  <section class="billboard">
    <svg class="billboard-shapes" viewBox="0 0 985 429" aria-hidden="false">
      <defs>
        <linearGradient id="photo-tones" x1="0" y1="0" x2="1" y2="0.6">
          <stop offset="0" stop-color="var(--photo-dark)"/>
          <stop offset="0.55" stop-color="var(--photo-mid)"/>
          <stop offset="1" stop-color="var(--photo-light)"/>
        </linearGradient>
      </defs>
      <polygon class="corner-triangle" points="497,429 533,360 548,429" fill="var(--stripe)"/>
      <polygon class="diagonal-stripe" points="471,0 495,0 594,429 570,429" fill="var(--stripe)"/>
      <polygon class="photo-area" role="img" aria-label="Photo of a smiling elderly woman and a younger caregiver with an arm around her shoulders, outdoors among trees" points="520,0 985,0 985,305 589,305" fill="url(#photo-tones)"/>
      <polygon class="contact-panel" points="589,305 985,305 985,429 617,429" fill="var(--panel)"/>
      <polygon class="edge-band" points="589,305 614,305 643,429 617,429" fill="var(--deep)"/>
    </svg>

    <div class="brand">
      <span class="brand-dot"></span>
      <span class="brand-name">Harbor Lane Home Aides</span>
    </div>

    <h1 class="headline">
      Help keep Hoosiers<br>
      <span class="highlight">Happy</span> and <span class="highlight">at home !</span>
    </h1>

    <p class="message">
      "EMPOWERING FRIENDS AND FAMILY TO CARE<br>
      FOR THEIR LOVED ONES AT HOME. ELIGIBLE PARTICIPANTS<br>
      RECEIVE UP TO <span class="highlight">$15,000</span> A YEAR, <span class="highlight">TAX FREE."</span>
    </p>

    <div class="contact">
      <p class="contact-label">CALL US :</p>
      <p class="contact-phone">00 555 014 227</p>
    </div>
  </section>
</body>
</html>
```